Vermilion Reel Works Web Design

COMPANY: VERMILION REEL WORKS
LOCATION: SHANGHAI, CHINA
AREA: FILM/TV DRAMA/COMMERCIALS/GAME POST PRODUCTION, SOUND DESIGN, MUSIC, and GAME.
WEB STYLE: SIMPLE, PROFESSIONAL, TRUSTWORTHY

LANGUAGE: ENGLISH, CHINESE. (Same layout, different language)
UPDATE: AFTER PROJECT FINISHED, WE NEED UPDATE BY OURSELVES.

MAIN SUBJECT: 6
1 HOMEPAGE
2 ABOUT US
3 TEAM
4 SERVICES
5 FACILITY
6 CONTACT

add one page of JOB OPPORTUNITIES.

DETAILS
1 HOMEPAGE
SLOGAN: Vermilion Reel Works provides a well-designed working environment which amplifies your team’s ability to reach their creative goals.

Our services include:
 Feature Films
 Music & Scoring
 Commercials
 ADR & Foley
 Sound & Picture Editorial
 Sound Design
 Video Game

2 ABOUT US
Vermilion Reel Works is located in the premiere South-Bund area of Shanghai. Occupying a 5000 square meter Technical Building, Vermilion Reel Works was built by a filmmaker for filmmakers, and is one of the largest, most versatile full-service post-production facilities in China.

Vermilion Reel Works is positioning to be at the forefront of the latest technology. Our goal is to provide a comprehensive solution for the post-production needs of our clients. We offer two fully-equipped dubbing stages (one of which will be certified KESTRON VOXAR PREMIERE), a large variety of both picture and sound editing rooms, impressive Foley and ADR stages, a world-class scoring stage, and complete audio and video transfer services.

We can handle your entire project from editing all the way to the end of the final sound mix; all under one extremely comfortable roof. We fully realize that the true art is in listening to the needs of our clients and making their greatest vision a reality. To this end our creative team's expertise, with a network of sound supervisors, editors and mixers, will deliver the magic you need. Producers and directors will also find our richly appointed guest accommodations to be a comfortable and soothing place to wind up the day. Every aspect of your project will be taken care of by a skilled and dedicated team, in the way that is best suited to you.

3 TEAM
(attachment 01)

4 SERVICES
Sound Mix
ADR
FOLEY
MUSIC
Sound Design
Sound Edit
Picture Edit
for all the Films, TV Drama, Commercials, Video Games, Online Media
(attachment 02, use photo)

5 FACILITY
(attachment 03)

6 CONTACT
(attachment04)
with map

Project Deadline Extended
Reason: Designers work are great, my bosses will spend 1-2 days select one of these web design, and spend 1-2 days to make some change, maybe use new photos.

```html
<!DOCTYPE html>
<html lang="en">
<head>
<meta charset="utf-8">
<title>Vermilion Reel Works</title>
<link href="https://fonts.googleapis.com/css2?family=Montserrat:wght@600;700&family=Open+Sans:wght@400;600&family=Bree+Serif&family=PT+Serif&family=Raleway:wght@500&display=swap" rel="stylesheet">
<style>
:root{
  --navy:#1f3a6e;
  --blue:#0b4aa0;
  --ink:#222;
  --text:#777;
  --muted:#999;
  --white:#fff;
  --dark-band:rgba(10,10,10,.82);
  --footer:#f3f3f3;
  --line:#e2e2e2;
  --quote:#e4e4e4;
  --accent:#2bb3e6;
}
*{margin:0;padding:0;box-sizing:border-box}
html,body{width:751px;height:1200px;overflow:hidden;background:var(--white)}
body{font-family:"Open Sans",sans-serif;color:var(--text);position:relative}
.abs{position:absolute}

/* header */
.site-header{left:0;top:0;width:751px;height:47px;background:var(--white)}
.brand{left:86px;top:14px;font-family:"Open Sans",sans-serif;font-size:15px;color:var(--ink);letter-spacing:.3px;display:flex;align-items:center;gap:6px}
.brand-mark{width:10px;height:10px;background:var(--navy)}
.main-nav{right:86px;top:17px;display:flex;gap:23px;font-size:8.5px;color:var(--muted)}
.main-nav .active{color:var(--navy);border-bottom:1px solid var(--navy)}

/* hero */
.hero{left:0;top:47px;width:751px;height:367px;background:linear-gradient(100deg,#5a4a3c 0%,#3d342c 30%,#2a2420 55%,#4a3a26 80%,#2a241c 100%)}
.hero-title{left:338px;top:98px;font-family:"Montserrat",sans-serif;font-weight:700;font-size:29px;line-height:29px;color:var(--white)}
.hero-sub{left:338px;top:166px;font-size:15.5px;color:var(--white)}
.btn{display:flex;align-items:center;justify-content:center;font-family:"Open Sans",sans-serif;font-weight:600}
.btn-hero-primary{left:339px;top:205px;width:116px;height:29px;background:var(--blue);color:var(--white);font-size:10px}
.btn-hero-light{left:468px;top:205px;width:116px;height:29px;background:var(--white);color:var(--ink);font-size:10px}

.service-band{left:0;top:274px;width:751px;height:140px;background:var(--dark-band)}
.service{width:160px;text-align:center;color:var(--white)}
.service svg{display:block;margin:0 auto}
.service h3{font-family:"Raleway",sans-serif;font-weight:500;font-size:13px;margin-top:6px}
.service p{font-size:6.4px;line-height:9.2px;margin-top:6px}

/* sound what */
.section-title{left:86px;top:466px;font-family:"Bree Serif",serif;font-size:36px;color:#3a3a3a}
.icon-strip{left:87px;top:525px;width:21px;border:1px solid #d5d5d5;background:#f7f7f7}
.icon-strip div{height:15px;border-bottom:1px solid #ddd;display:flex;align-items:center;justify-content:center}
.icon-strip div:last-child{border-bottom:none}
.lead-copy{left:140px;top:524px;width:302px;font-family:"PT Serif",serif;font-size:7.3px;line-height:12.7px;color:var(--muted)}
.pull-quote{left:140px;top:591px;width:290px;border-left:2px solid #ddd;padding-left:10px;font-family:"PT Serif",serif;font-size:7.3px;line-height:12px;color:var(--muted)}
.pull-quote cite{display:block;font-style:normal;color:var(--accent)}
.btn-navy{background:var(--navy);color:var(--white);font-family:"Raleway",sans-serif;font-weight:500;font-size:9.5px}
.btn-sound{left:140px;top:632px;width:85px;height:19px}
.device-shot{left:465px;top:450px;width:200px;height:186px;background:linear-gradient(135deg,#f2f2f2,#d6d6d6 45%,#3a3a3a 60%,#cfcfcf);border-radius:10px}

/* banner */
.banner{left:0;top:702px;width:751px;height:184px;background:linear-gradient(90deg,#6d5450 0%,#4a3c3c 35%,#6a5a52 70%,#8a7a70 100%)}
.banner-title{left:352px;top:739px;font-family:"Montserrat",sans-serif;font-weight:700;font-size:21px;color:var(--white)}
.banner-copy{left:352px;top:771px;width:312px;font-size:8.6px;line-height:10.4px;color:var(--white)}
.btn-banner{left:353px;top:812px;width:85px;height:19px}

/* testimonial */
.avatar{left:342px;top:920px;width:58px;height:58px;border-radius:50%;background:radial-gradient(circle at 50% 40%,#f4dcc8,#d8b690 70%,#bfa080);border:2px solid #eee}
.quote-mark{font-family:Georgia,serif;font-size:64px;line-height:1;color:var(--quote)}
.quote-open{left:84px;top:962px}
.quote-close{left:630px;top:1010px}
.testimonial-copy{left:118px;top:994px;width:516px;text-align:center;font-size:8.6px;line-height:12.8px;color:var(--muted)}
.testimonial-rule{left:150px;top:1046px;width:450px;height:6px;background:radial-gradient(ellipse at center top,rgba(0,0,0,.08),transparent 70%)}
.testimonial-name{left:0;top:1064px;width:751px;text-align:center;font-family:"Raleway",sans-serif;font-weight:500;font-size:14px;color:var(--navy)}

/* footer */
.site-footer{left:0;top:1107px;width:751px;height:93px;background:var(--footer);border-top:1px solid var(--line)}
.footer-brand{left:88px;top:1125px}
.footer-nav{right:86px;top:1127px;display:flex;gap:8px;font-size:7.8px;color:var(--muted)}
.footer-rule{left:0;top:1169px;width:751px;height:1px;background:var(--line)}
.copyright{left:86px;top:1181px;font-size:7.5px;color:var(--muted)}
.legal-nav{right:96px;top:1179px;display:flex;gap:8px;font-size:7.2px;color:var(--muted)}
</style>
</head>
<body>

<header class="site-header abs">
  <div class="brand abs"><span class="brand-mark"></span>Vermilion Reel Works</div>
  <nav class="main-nav abs">
    <span class="active">Home</span><span>About Us</span><span>Team</span><span>Services</span><span>Facility</span><span>Contact</span>
  </nav>
</header>

<section class="hero abs" role="img" aria-label="Sound engineer working at a mixing console in a dim post-production studio"></section>
<h1 class="hero-title abs">Welcome to the<br>Vermilion Reel Works</h1>
<p class="hero-sub abs">Sed ut perspiciatis unde omnis iste natus error</p>
<div class="btn btn-hero-primary abs">How It Works?</div>
<div class="btn btn-hero-light abs">Read More</div>

<section class="service-band abs">
  <div class="service abs" style="left:81px;top:17px">
    <svg width="32" height="36" viewBox="0 0 32 36"><circle cx="9" cy="7" r="6" fill="#fff"/><circle cx="19" cy="7" r="6" fill="#fff"/><rect x="3" y="12" width="20" height="11" fill="#fff"/><path d="M23 15l7-4v12l-7-4z" fill="#fff"/><path d="M13 23l-6 12M13 23l6 12M13 23v12" stroke="#fff" stroke-width="2"/></svg>
    <h3>Feature Films</h3>
    <p>Sed ut perspiciatis unde omnis iste natus error sit totam rem aperiam, eaque ipsa quae ab illo inventore veritatis et quasi explicabo.</p>
  </div>
  <div class="service abs" style="left:295px;top:17px">
    <svg width="40" height="36" viewBox="0 0 40 36"><path d="M0 18h4l2-4 2 8 2-10 2 12 3-18 3 24 2-20 2 16 2-12 3 16 2-10 2 6 2-4 2 2h7" stroke="#fff" stroke-width="1.6" fill="none"/></svg>
    <h3>Music &amp; Scoring</h3>
    <p>Sed ut perspiciatis unde omnis iste natus error sit totam rem aperiam, eaque ipsa quae ab illo inventore veritatis et quasi explicabo.</p>
  </div>
  <div class="service abs" style="left:510px;top:17px">
    <svg width="34" height="36" viewBox="0 0 34 36"><rect x="9" y="2" width="16" height="32" rx="2" fill="none" stroke="#fff" stroke-width="2"/><circle cx="17" cy="10" r="3" fill="#fff"/><circle cx="17" cy="23" r="6" fill="none" stroke="#fff" stroke-width="2"/><circle cx="17" cy="23" r="2" fill="#fff"/><path d="M5 14q-3 6 0 12M2 11q-4 9 0 18M29 14q3 6 0 12M32 11q4 9 0 18" stroke="#fff" stroke-width="1.4" fill="none"/></svg>
    <h3>Commercials</h3>
    <p>Sed ut perspiciatis unde omnis iste natus error sit totam rem aperiam, eaque ipsa quae ab illo inventore veritatis et quasi explicabo.</p>
  </div>
</section>

<h2 class="section-title abs">Sound What?</h2>
<div class="icon-strip abs">
  <div><svg width="8" height="7" viewBox="0 0 8 7"><path d="M4 7L0.5 3.2A2 2 0 0 1 4 1a2 2 0 0 1 3.5 2.2z" fill="#333"/></svg></div>
  <div><svg width="8" height="8" viewBox="0 0 8 8"><circle cx="4" cy="4" r="3.2" fill="none" stroke="#333" stroke-width="1.2"/><path d="M4 2v2h1.6" stroke="#333" stroke-width="1"/></svg></div>
  <div><svg width="8" height="8" viewBox="0 0 8 8"><path d="M1 7l1-3 4-4 2 2-4 4z" fill="#333"/></svg></div>
  <div><svg width="8" height="8" viewBox="0 0 8 8"><circle cx="4" cy="2.3" r="2" fill="#333"/><path d="M0.5 8a3.5 3.5 0 0 1 7 0z" fill="#333"/></svg></div>
</div>
<p class="lead-copy abs">Lorem ipsum dolor sit amet, consectetuer adipiscing elit, sed diam nonummy nibh euismod tincidunt ut laoreet dolore magna aliquam erat volutpat. Ut wisi enim ad minim veniam, quis nostrud exerci tation ullamcorper suscipit lobortis nisl ut aliquip ex ea commodo consequat. Duis autem vel eum iriure dolor in he.</p>
<blockquote class="pull-quote abs">Lorem ipsum dolor sit amet, consectetur adipiscing elit. Integer posuere erat a ante.<cite>— Lena Corvath</cite></blockquote>
<div class="btn btn-navy btn-sound abs">Read More</div>
<div class="device-shot abs" role="img" aria-label="Two smartphones showing close-up photos of studio audio equipment"></div>

<section class="banner abs" role="img" aria-label="Blurred close-up of mixing console faders"></section>
<h2 class="banner-title abs">Vermilion Reel Works provides</h2>
<p class="banner-copy abs">Sed ut perspiciatis unde omnis iste natus error sit totam rem aperiam, eaque ipsa quae ab illo inventore veritatis et quasi architecto beatae vitae dicta sunt explicabo sed quia non numquam</p>
<div class="btn btn-navy btn-banner abs">Read More</div>

<div class="avatar abs" role="img" aria-label="Portrait photo of the quoted client"></div>
<div class="quote-mark quote-open abs">&ldquo;</div>
<div class="quote-mark quote-close abs">&rdquo;</div>
<p class="testimonial-copy abs">Lorem ipsum dolor sit amet, consectetur adipiscing elit, sed do eiusmod tempor incididunt ut labore et dolore magna aliqua. Ut enim ad minim veniam, quis nostrud exercitation ullamco laboris nisi ut aliquip ex ea commodo consequat. Duis aute irure dolor in reprehenderit in voluptate velit esse cillum dolore eu fugiat nulla pariatur..</p>
<div class="testimonial-rule abs"></div>
<p class="testimonial-name abs">Marco Veltrani, CEO</p>

<footer class="site-footer abs"></footer>
<div class="brand footer-brand abs"><span class="brand-mark"></span>Vermilion Reel Works</div>
<nav class="footer-nav abs">
  <span>Home</span><span>|</span><span>Our Services</span><span>|</span><span>Advices</span><span>|</span><span>Programming</span><span>|</span><span>Support us</span><span>|</span><span>Contact Us</span>
</nav>
<div class="footer-rule abs"></div>
<p class="copyright abs">Copyrights © 2014 Vermilion Reel Works.com - All Rights Reserved</p>
<nav class="legal-nav abs"><span>Privacy Policy</span><span>|</span><span>Terms &amp; Conditions</span></nav>

</body>
</html>
```